Redesign Power Point Template

we would like to update our powerpoint template. The current design limits the available space. we would like to keep the same colors and logo but have more room for content. We need both standard and cover template. I have attached our current template. we do not want to include the tag line "change your perspective" or the graph.

```html
<!DOCTYPE html>
<html lang="en">
<head>
<meta charset="utf-8">
<title>Talvorix Presentation Template</title>
<link href="https://fonts.googleapis.com/css2?family=Montserrat:wght@400;600;700;800&family=Open+Sans:wght@400;600;700&display=swap" rel="stylesheet">
<style>
:root{
  --green-dark:#1d3a19;
  --green:#4f8f35;
  --green-mid:#6aa84f;
  --green-light:#a9cf8f;
  --green-pale:#dcebd0;
  --grey:#b9b9b9;
  --grey-light:#e4e4e4;
  --page:#e9e9e9;
  --ink:#2a2a2a;
  --white:#ffffff;
  --gold:#c9a227;
}
*{box-sizing:border-box;margin:0;padding:0}
html,body{width:1200px;height:3409px;overflow:hidden;background:var(--page)}
body{position:relative;font-family:"Open Sans",Arial,sans-serif;color:var(--ink)}
.slide{position:absolute;width:568px;height:320px;background:var(--white);overflow:hidden;box-shadow:0 1px 3px rgba(0,0,0,.15)}
.slide p{font-size:6.2px;line-height:1.45;color:#444}
.heading{font-family:"Montserrat",Arial,sans-serif;font-size:13px;font-weight:400;color:#111;position:absolute;left:16px;top:12px}
.heading b{font-weight:800}
.foot{position:absolute;left:0;right:0;bottom:0;height:9px;background:var(--green)}
.foot-tag{position:absolute;right:10px;bottom:3px;background:var(--white);padding:2px 8px;font-family:"Montserrat",Arial,sans-serif;font-weight:800;font-size:8px;color:var(--green-dark)}
.brand{font-family:"Montserrat",Arial,sans-serif;font-weight:800;color:var(--green-dark);display:flex;align-items:center;gap:6px}
.brand i{display:inline-block;background:var(--green)}
.tile-art{position:absolute;background:linear-gradient(135deg,var(--grey-light),var(--grey) 45%,var(--green-pale) 70%,var(--grey-light))}
.photo{position:absolute;background:linear-gradient(135deg,#d9ddd6,#9fa79a 55%,#eef0ec)}
.photo.warm{background:linear-gradient(135deg,#f2f2f0,#c9cbc5 50%,#8c8f88)}
.photo.green{background:linear-gradient(135deg,#3d6a2e,#7fae63 55%,#2c4d22)}
.col{position:absolute}
.col p+p{margin-top:7px}
.title-w{font-family:"Montserrat",Arial,sans-serif;font-weight:400;color:var(--white);font-size:17px;line-height:1.15}
.title-w b{font-weight:800}
.panel-dark{position:absolute;background:var(--green-dark)}
.panel{position:absolute;background:var(--green-mid)}
.ico{width:22px;height:22px;border-radius:50%;background:var(--green-dark);display:flex;align-items:center;justify-content:center;flex:none}
.ico svg{width:12px;height:12px}
.service{background:#fff;height:52px;display:flex;flex-direction:column;align-items:center;justify-content:center;gap:4px;font-size:4.6px;text-align:center}
.step{display:flex;align-items:center}
.step-num{width:20px;height:20px;border-radius:50%;border:2px solid var(--green);background:#fff;font-size:8px;font-weight:700;display:flex;align-items:center;justify-content:center;z-index:1}
.step-bar{flex:1;margin-left:-6px;color:#fff;font-size:6px;padding:4px 12px}
.feature-ico{width:38px;height:38px;border-radius:50%;background:#fff;border:2px solid var(--green-dark);margin:0 auto;display:flex;align-items:center;justify-content:center}
.feature-title{font-size:6.5px;font-weight:700;margin:8px 0 3px}
.point{display:flex;gap:12px;align-items:flex-start}
.point-title{font-size:7px;font-weight:700;color:var(--green)}
.member-photo{width:84px;height:78px;margin:0 auto;background:linear-gradient(180deg,#d0d0d0,#8a8a8a)}
.member-name{background:var(--green);color:#fff;font-size:6px;font-weight:700;padding:2px;margin:4px 20px 2px}
.member-role{font-size:5.5px;color:var(--green)}
</style>
</head>
<body>

<section class="slide" style="left:298px;top:18px;width:568px;height:327px">
  <div style="position:absolute;left:0;right:0;top:0;height:7px;background:var(--green)"></div>
  <div class="tile-art" style="left:330px;top:7px;width:238px;height:140px;clip-path:polygon(20% 0,100% 0,100% 100%,60% 90%,35% 40%)" role="img" aria-label="Decorative grey and green tile mosaic"></div>
  <div style="position:absolute;left:0;bottom:10px;width:140px;height:100px;background:var(--green-dark);clip-path:polygon(0 0,100% 100%,0 100%)"></div>
  <div style="position:absolute;left:0;bottom:10px;width:110px;height:60px;background:var(--green-mid);clip-path:polygon(0 20%,100% 100%,0 100%)"></div>
  <div style="position:absolute;left:0;right:0;bottom:0;height:10px;background:var(--green)"></div>
  <div class="brand" style="position:absolute;left:0;right:0;top:120px;justify-content:center;font-size:30px"><i style="width:18px;height:18px"></i>Talvorix</div>
  <div style="position:absolute;left:0;right:0;top:160px;text-align:center;font-size:6px;color:#555">prescription benefit management</div>
</section>

<section class="slide" style="left:305px;top:364px;width:559px;height:322px">
  <div class="photo warm" style="inset:0" role="img" aria-label="Business handshake with team in background"></div>
  <div style="position:absolute;left:150px;top:70px;width:260px;height:110px;background:rgba(255,255,255,.75)"></div>
  <div class="brand" style="position:absolute;left:150px;width:260px;top:100px;justify-content:center;font-size:30px"><i style="width:18px;height:18px"></i>Talvorix</div>
  <div style="position:absolute;left:150px;width:260px;top:140px;text-align:center;font-size:6px;color:#555">prescription benefit management</div>
</section>

<section class="slide" style="left:18px;top:705px">
  <div class="heading" style="font-size:10px"><b>Talvorix's Complete Services Package</b></div>
  <div class="col" style="left:16px;top:40px;width:230px">
    <p>Ut wisi enim ad minim veniam, quis nostrud exerci tation ullamcorper suscipit lobortis nisl ut aliquip ex ea commodo consequat duis autem vel eum.</p>
    <p>Lorem ipsum dolor sit amet, consectetur adipiscing elit, sed do eiusmod tempor incididunt ut labore et dolore magna aliqua.</p>
    <p>Ut wisi enim ad minim veniam, quis nostrud exerci tation ullamcorper suscipit lobortis nisl ut aliquip ex ea commodo consequat duis autem vel eum.</p>
    <p>Lorem ipsum dolor sit amet, consectetur adipiscing elit, sed do eiusmod tempor incididunt ut labore et dolore magna aliqua.</p>
    <p>Ut wisi enim ad minim veniam, quis nostrud exerci tation ullamcorper suscipit lobortis nisl ut aliquip ex ea commodo consequat duis autem vel eum.</p>
  </div>
  <div class="panel-dark" style="left:272px;top:20px;width:282px;height:278px;padding:12px 14px">
    <div style="font-size:6.5px;color:#fff;font-weight:700">Lorem ipsum dolor sit amet, consectetur adipiscing elit</div>
    <p style="color:#cfdcc8;margin-top:4px">Ut wisi enim ad minim veniam, quis nostrud exerci tation ullamcorper suscipit lobortis nisl ut aliquip ex ea commodo.</p>
    <div style="display:grid;grid-template-columns:repeat(3,56px);gap:12px 16px;margin:14px 0 0 22px">
      <div class="service"><div class="ico"><svg viewBox="0 0 12 12"><rect x="2" y="1" width="8" height="10" fill="none" stroke="#fff"/><path d="M4 4h4M4 6h4M4 8h3" stroke="#fff"/></svg></div>Claims Processing</div>
      <div class="service"><div class="ico"><svg viewBox="0 0 12 12"><circle cx="6" cy="3" r="2" fill="#fff"/><circle cx="2.5" cy="9" r="1.7" fill="#fff"/><circle cx="9.5" cy="9" r="1.7" fill="#fff"/><path d="M6 5L3 8M6 5l3 3" stroke="#fff"/></svg></div>Provider Network Management</div>
      <div class="service"><div class="ico"><svg viewBox="0 0 12 12"><path d="M2 10l3-4 2 2 3-5" stroke="#fff" fill="none"/></svg></div>Benefit Design Consulting</div>
      <div class="service"><div class="ico"><svg viewBox="0 0 12 12"><rect x="2" y="6" width="2" height="4" fill="#fff"/><rect x="5" y="3" width="2" height="7" fill="#fff"/><rect x="8" y="5" width="2" height="5" fill="#fff"/></svg></div>Analytics</div>
      <div class="service"><div class="ico"><svg viewBox="0 0 12 12"><path d="M6 2v8M2 6h8" stroke="#fff" stroke-width="2"/></svg></div>Clinical Consultative Services</div>
      <div class="service"><div class="ico"><svg viewBox="0 0 12 12"><path d="M3 6h6M6 3l3 3-3 3" stroke="#fff" fill="none"/></svg></div>What's Next for Rx?</div>
    </div>
  </div>
  <div class="foot"></div><div class="foot-tag">Talvorix</div>
</section>

<section class="slide" style="left:614px;top:705px">
  <div class="heading"><b>Lorem ipsum</b> dolor sit amet</div>
  <div class="tile-art" style="left:330px;top:0;width:238px;height:110px;clip-path:polygon(10% 0,100% 0,100% 100%,45% 70%)" role="img" aria-label="Decorative grey and green tile mosaic"></div>
  <div style="position:absolute;left:8px;top:42px;width:300px;display:flex;flex-direction:column;gap:8px">
    <div class="step"><span class="step-num">1</span><span class="step-bar" style="background:var(--green-dark)">This is a sample text. Enter Your text Here</span></div>
    <div class="step"><span class="step-num">2</span><span class="step-bar" style="background:var(--green-mid)">This is a sample text. Enter Your text Here</span></div>
    <div class="step"><span class="step-num">3</span><span class="step-bar" style="background:var(--green-dark)">This is a sample text. Enter Your text Here</span></div>
    <div class="step"><span class="step-num">4</span><span class="step-bar" style="background:var(--green-mid)">This is a sample text. Enter Your text Here</span></div>
    <div class="step"><span class="step-num">5</span><span class="step-bar" style="background:var(--green-dark)">This is a sample text. Enter Your text Here</span></div>
  </div>
  <div class="col" style="left:340px;top:112px;width:200px"><p>Lorem ipsum dolor sit amet, consectetur adipiscing elit. Curabitur et eros facilisis, molestie velit sed, egestas tortor. Pellentesque nisl augue, molestie non tincidunt elementum, faucibus et mauris. Maecenas a libero eu diam condimentum tristique. Pellentesque nisl augue, molestie non tincidunt elementum, faucibus et mauris. Maecenas a libero eu diam condimentum tristique.</p></div>
  <div class="foot"></div><div class="foot-tag">Talvorix</div>
</section>

<section class="slide" style="left:18px;top:1027px">
  <div class="photo" style="left:0;top:0;width:260px;height:170px" role="img" aria-label="Business people working at a laptop"></div>
  <div class="panel" style="left:240px;top:0;width:328px;height:170px;background:rgba(79,143,53,.92);padding:28px 30px">
    <div class="title-w"><b>Lorem ipsum<br>dolor sit amet</b></div>
    <p style="color:#eef5e9;margin-top:8px;width:190px">Ut wisi enim ad minim veniam, quis nostrud exerci tation ullamcorper suscipit lobortis nisl ut aliquip ex ea commodo consequat.</p>
  </div>
  <div class="col" style="left:16px;top:192px;width:250px"><p>Lorem ipsum dolor sit amet, consectetur adipiscing elit. Curabitur et eros facilisis, molestie velit sed, egestas tortor. Pellentesque nisl augue, molestie non tincidunt elementum, faucibus et mauris. Maecenas a libero eu diam condimentum tristique.</p></div>
  <div class="col" style="left:300px;top:192px;width:250px"><p>Lorem ipsum dolor sit amet, consectetur adipiscing elit. Curabitur et eros facilisis, molestie velit sed, egestas tortor. Pellentesque nisl augue, molestie non tincidunt elementum, faucibus et mauris. Maecenas a libero eu diam condimentum tristique.</p></div>
  <div class="foot"></div><div class="foot-tag">Talvorix</div>
</section>

<section class="slide" style="left:614px;top:1027px">
  <div class="photo warm" style="left:0;top:24px;width:320px;height:250px" role="img" aria-label="Pharmacist working at a computer"></div>
  <div class="panel-dark" style="left:300px;top:0;width:268px;height:282px;padding:38px 22px">
    <div class="title-w">Lorem ipsum<br><b>dolor sit amet</b></div>
    <p style="color:#d9e5d2;margin-top:10px">Lorem ipsum dolor sit amet, consectetur adipiscing elit. Curabitur et eros facilisis, molestie velit sed, egestas tortor. Pellentesque nisl augue, molestie non tincidunt elementum, faucibus et mauris. Maecenas a libero eu diam condimentum tristique.</p>
  </div>
  <div class="foot"></div><div class="foot-tag">Talvorix</div>
</section>

<section class="slide" style="left:18px;top:1355px">
  <div class="photo warm" style="left:200px;top:0;width:368px;height:320px" role="img" aria-label="Two laboratory staff in white coats"></div>
  <div class="panel" style="left:0;top:62px;width:292px;height:190px;background:var(--green-light);padding:28px 30px">
    <div class="title-w">Lorem ipsum <b>dolor<br>sit amet</b></div>
    <p style="color:#fff;margin-top:10px;width:220px">Lorem ipsum dolor sit amet, consectetur adipiscing elit, sed do eiusmod tempor incididunt ut labore et dolore magna aliqua. Ut enim ad minim veniam, quis nostrud exercitation ullamco laboris nisi ut aliquip ex ea commodo consequat.</p>
  </div>
  <div class="foot"></div><div class="foot-tag">Talvorix</div>
</section>

<section class="slide" style="left:614px;top:1355px">
  <div class="photo green" style="left:0;top:0;width:568px;height:178px" role="img" aria-label="Laboratory scene with green overlay"></div>
  <div style="position:absolute;left:0;right:0;top:38px;text-align:center" class="title-w"><b>Lorem ipsum dolor</b> sit amet</div>
  <p style="position:absolute;left:120px;width:330px;top:66px;text-align:center;color:#e6f0e0">Lorem ipsum dolor sit amet, consectetur adipiscing elit, sed do eiusmod tempor incididunt ut labore et dolore magna aliqua.</p>
  <div style="position:absolute;left:30px;right:30px;top:152px;display:grid;grid-template-columns:repeat(4,1fr);gap:14px;text-align:center">
    <div><div class="feature-ico"><svg width="18" height="18" viewBox="0 0 12 12"><rect x="2" y="5" width="8" height="5" fill="#1d3a19"/><path d="M1 5l5-3 5 3" fill="#1d3a19"/></svg></div><div class="feature-title">Lorem ipsum dolor</div><p>Lorem ipsum dolor sit amet, consectetur adipiscing elit, sed do eiusmod tempor.</p></div>
    <div><div class="feature-ico"><svg width="18" height="18" viewBox="0 0 12 12"><circle cx="6" cy="6" r="4.5" fill="none" stroke="#1d3a19" stroke-width="1.5"/><circle cx="6" cy="6" r="1.6" fill="#1d3a19"/></svg></div><div class="feature-title">Lorem ipsum dolor</div><p>Lorem ipsum dolor sit amet, consectetur adipiscing elit, sed do eiusmod tempor.</p></div>
    <div><div class="feature-ico"><svg width="18" height="18" viewBox="0 0 12 12"><path d="M2 2l8 8M10 2l-8 8" stroke="#1d3a19" stroke-width="2"/></svg></div><div class="feature-title">Lorem ipsum dolor</div><p>Lorem ipsum dolor sit amet, consectetur adipiscing elit, sed do eiusmod tempor.</p></div>
    <div><div class="feature-ico"><svg width="18" height="18" viewBox="0 0 12 12"><circle cx="4" cy="4" r="2" fill="#1d3a19"/><circle cx="8.5" cy="4" r="2" fill="#1d3a19"/><path d="M0.5 11c0-3 7-3 7 0M5 11c0-3 7-3 7 0" fill="#1d3a19"/></svg></div><div class="feature-title">Lorem ipsum dolor</div><p>Lorem ipsum dolor sit amet, consectetur adipiscing elit, sed do eiusmod tempor.</p></div>
  </div>
  <div class="foot"></div><div class="foot-tag">Talvorix</div>
</section>

<section class="slide" style="left:18px;top:1682px">
  <div class="heading"><b>Lorem ipsum</b> dolor sit amet</div>
  <div class="col" style="left:16px;top:42px;width:160px"><p>Lorem ipsum dolor sit amet, consectetur adipiscing elit, sed do eiusmod tempor incididunt ut labore et dolore magna aliqua. Ut enim ad minim veniam, quis nostrud exercitation.</p><p>Ut wisi enim ad minim veniam, quis nostrud exerci tation ullamcorper suscipit lobortis nisl ut aliquip ex ea.</p><p>Lorem ipsum dolor sit amet, consectetur adipiscing elit, sed do eiusmod tempor incididunt ut labore et dolore magna aliqua. Ut enim ad minim veniam.</p></div>
  <div class="panel-dark" style="left:190px;top:36px;width:140px;height:262px;padding:52px 14px 0 24px">
    <div style="display:flex;flex-direction:column;gap:26px">
      <div style="display:flex;gap:8px"><svg width="8" height="10" viewBox="0 0 8 10" style="flex:none"><path d="M0 0l8 5-8 5z" fill="#a9cf8f"/></svg><p style="color:#dbe8d3">Lorem ipsum dolor sit amet, consectetur adipiscing elit, sed do.</p></div>
      <div style="display:flex;gap:8px"><svg width="8" height="10" viewBox="0 0 8 10" style="flex:none"><path d="M0 0l8 5-8 5z" fill="#a9cf8f"/></svg><p style="color:#dbe8d3">Lorem ipsum dolor sit amet, consectetur adipiscing elit, sed do.</p></div>
      <div style="display:flex;gap:8px"><svg width="8" height="10" viewBox="0 0 8 10" style="flex:none"><path d="M0 0l8 5-8 5z" fill="#a9cf8f"/></svg><p style="color:#dbe8d3">Lorem ipsum dolor sit amet, consectetur adipiscing elit, sed do.</p></div>
    </div>
  </div>
  <div class="col" style="left:350px;top:42px;width:200px"><p>Lorem ipsum dolor sit amet, consectetur adipiscing elit, sed do eiusmod tempor incididunt ut labore et dolore magna aliqua.</p>
    <div style="display:flex;flex-direction:column;gap:16px;margin-top:22px">
      <div style="display:flex;gap:10px"><svg width="10" height="10" viewBox="0 0 10 10" style="flex:none"><path d="M0 0l10 5-10 5z" fill="#4f8f35"/></svg><p>Lorem ipsum dolor sit amet, consectetur adipiscing elit, sed do eiusmod tempor.</p></div>
      <div style="display:flex;gap:10px"><svg width="10" height="10" viewBox="0 0 10 10" style="flex:none"><path d="M0 0l10 5-10 5z" fill="#4f8f35"/></svg><p>Lorem ipsum dolor sit amet, consectetur adipiscing elit, sed do eiusmod tempor.</p></div>
      <div style="display:flex;gap:10px"><svg width="10" height="10" viewBox="0 0 10 10" style="flex:none"><path d="M0 0l10 5-10 5z" fill="#4f8f35"/></svg><p>Lorem ipsum dolor sit amet, consectetur adipiscing elit, sed do eiusmod tempor.</p></div>
    </div>
  </div>
  <div class="foot"></div><div class="foot-tag">Talvorix</div>
</section>

<section class="slide" style="left:614px;top:1682px">
  <div class="heading"><b>Lorem ipsum</b> dolor sit amet</div>
  <div style="position:absolute;left:16px;right:16px;top:42px;display:grid;grid-template-columns:repeat(4,1fr);gap:16px">
    <div><p>Lorem ipsum dolor sit amet, consectetur adipiscing elit, sed do eiusmod tempor incididunt ut labore et dolore magna aliqua. Ut enim ad minim veniam, quis nostrud exercitation ullamco.</p><p style="margin-top:7px">Ea commodo consequat. Lorem ipsum dolor sit amet, consectetur adipiscing elit, sed do eiusmod tempor incididunt ut labore.</p><p style="margin-top:7px">Lorem ipsum dolor sit amet, consectetur adipiscing elit, sed do eiusmod tempor incididunt ut labore et dolore magna aliqua. Ut enim ad minim veniam.</p></div>
    <div><p>Lorem ipsum dolor sit amet, consectetur adipiscing elit, sed do eiusmod tempor incididunt ut labore et dolore magna aliqua. Ut enim ad minim veniam, quis nostrud exercitation ullamco.</p><p style="margin-top:7px">Ea commodo consequat. Lorem ipsum dolor sit amet, consectetur adipiscing elit, sed do eiusmod tempor incididunt ut labore.</p><p style="margin-top:7px">Lorem ipsum dolor sit amet, consectetur adipiscing elit, sed do eiusmod tempor incididunt ut labore et dolore magna aliqua. Ut enim ad minim veniam.</p></div>
    <div><p>Lorem ipsum dolor sit amet, consectetur adipiscing elit, sed do eiusmod tempor incididunt ut labore et dolore magna aliqua. Ut enim ad minim veniam, quis nostrud exercitation ullamco.</p><p style="margin-top:7px">Ea commodo consequat. Lorem ipsum dolor sit amet, consectetur adipiscing elit, sed do eiusmod tempor incididunt ut labore.</p><p style="margin-top:7px">Lorem ipsum dolor sit amet, consectetur adipiscing elit, sed do eiusmod tempor incididunt ut labore et dolore magna aliqua. Ut enim ad minim veniam.</p></div>
    <div><p>Lorem ipsum dolor sit amet, consectetur adipiscing elit, sed do eiusmod tempor incididunt ut labore et dolore magna aliqua. Ut enim ad minim veniam, quis nostrud exercitation ullamco.</p><p style="margin-top:7px">Ea commodo consequat. Lorem ipsum dolor sit amet, consectetur adipiscing elit, sed do eiusmod tempor incididunt ut labore.</p><p style="margin-top:7px">Lorem ipsum dolor sit amet, consectetur adipiscing elit, sed do eiusmod tempor incididunt ut labore et dolore magna aliqua. Ut enim ad minim veniam.</p></div>
  </div>
  <div class="foot"></div><div class="foot-tag">Talvorix</div>
</section>

<section class="slide" style="left:18px;top:2014px">
  <div style="position:absolute;left:0;top:0;width:110px;height:311px;background:var(--green-dark);clip-path:polygon(0 0,100% 0,12% 100%,0 100%)"></div>
  <div style="position:absolute;right:0;top:0;width:70px;height:50px;background:var(--green-dark);clip-path:polygon(100% 0,100% 100%,0 0)"></div>
  <div class="heading" style="left:46px;top:12px;background:var(--white);padding:2px 8px"><b>Lorem ipsum</b> dolor sit amet</div>
  <div style="position:absolute;left:104px;top:58px;width:430px;display:flex;flex-direction:column;gap:22px">
    <div class="point"><div class="ico" style="background:#fff;border:1.5px solid var(--green-dark)"><svg viewBox="0 0 12 12"><circle cx="6" cy="5" r="3" fill="none" stroke="#1d3a19"/><path d="M5 9h2v2H5z" fill="#1d3a19"/></svg></div><div><div class="point-title">Lorem ipsum dolor sit amet</div><p>Lorem ipsum dolor sit amet, consectetur adipiscing elit, sed do eiusmod tempor incididunt ut labore et dolore magna aliqua.</p></div></div>
    <div class="point" style="margin-left:16px"><div class="ico" style="background:#fff;border:1.5px solid var(--green-dark)"><svg viewBox="0 0 12 12"><circle cx="6" cy="6" r="4" fill="none" stroke="#1d3a19"/><circle cx="6" cy="6" r="1.5" fill="#1d3a19"/></svg></div><div><div class="point-title">Lorem ipsum dolor sit amet</div><p>Lorem ipsum dolor sit amet, consectetur adipiscing elit, sed do eiusmod tempor incididunt ut labore et dolore magna aliqua.</p></div></div>
    <div class="point" style="margin-left:32px"><div class="ico" style="background:#fff;border:1.5px solid var(--green-dark)"><svg viewBox="0 0 12 12"><rect x="3" y="5" width="6" height="5" fill="#1d3a19"/><path d="M4 5V3.5a2 2 0 014 0V5" fill="none" stroke="#1d3a19"/></svg></div><div><div class="point-title">Lorem ipsum dolor sit amet</div><p>Lorem ipsum dolor sit amet, consectetur adipiscing elit, sed do eiusmod tempor incididunt ut labore et dolore magna aliqua.</p></div></div>
    <div class="point" style="margin-left:48px"><div class="ico" style="background:#fff;border:1.5px solid var(--green-dark)"><svg viewBox="0 0 12 12"><circle cx="6" cy="6" r="3" fill="none" stroke="#1d3a19" stroke-width="1.5"/><path d="M6 1v2M6 9v2M1 6h2M9 6h2" stroke="#1d3a19"/></svg></div><div><div class="point-title">Lorem ipsum dolor sit amet</div><p>Lorem ipsum dolor sit amet, consectetur adipiscing elit, sed do eiusmod tempor incididunt ut labore et dolore magna aliqua.</p></div></div>
  </div>
  <div class="foot"></div><div class="foot-tag">Talvorix</div>
</section>

<section class="slide" style="left:614px;top:2014px">
  <div class="photo warm" style="left:0;top:0;width:270px;height:320px;filter:grayscale(1)" role="img" aria-label="Medical staff in a clinic, black and white"></div>
  <div class="panel" style="left:24px;top:56px;width:226px;height:190px;background:rgba(106,168,79,.93);padding:28px 26px">
    <div class="title-w">Lorem ipsum dolor<br><b>sit amet</b></div>
    <p style="color:#fff;margin-top:10px">Lorem ipsum dolor sit amet, consectetur adipiscing elit, sed do eiusmod tempor incididunt ut labore et dolore magna aliqua. Ut enim ad minim veniam, quis nostrud exercitation ullamco laboris nisi ut aliquip ex ea commodo consequat.</p>
  </div>
  <div style="position:absolute;left:300px;top:42px;width:250px;display:flex;flex-direction:column;gap:20px">
    <div style="display:flex;gap:12px"><div class="ico" style="background:var(--grey)"><svg viewBox="0 0 12 12"><path d="M3 1h6L6 6l3 5H3l3-5z" fill="#fff"/></svg></div><p>Lorem ipsum dolor sit amet, consectetur adipiscing elit, sed do eiusmod tempor incididunt ut labore et dolore magna aliqua.</p></div>
    <div style="display:flex;gap:12px"><div class="ico" style="background:var(--grey)"><svg viewBox="0 0 12 12"><circle cx="6" cy="6" r="2" fill="#fff"/><path d="M6 1v3M6 8v3M1 6h3M8 6h3" stroke="#fff" stroke-width="1.5"/></svg></div><p>Lorem ipsum dolor sit amet, consectetur adipiscing elit, sed do eiusmod tempor incididunt ut labore et dolore magna aliqua.</p></div>
    <div style="display:flex;gap:12px"><div class="ico" style="background:var(--grey)"><svg viewBox="0 0 12 12"><circle cx="6" cy="6" r="4" fill="none" stroke="#fff" stroke-width="1.5"/><circle cx="6" cy="6" r="1.2" fill="#fff"/></svg></div><p>Lorem ipsum dolor sit amet, consectetur adipiscing elit, sed do eiusmod tempor incididunt ut labore et dolore magna aliqua.</p></div>
    <div style="display:flex;gap:12px"><div class="ico" style="background:var(--grey)"><svg viewBox="0 0 12 12"><rect x="2" y="4" width="8" height="6" fill="#fff"/><path d="M4 4V2.5h4V4" fill="none" stroke="#fff"/></svg></div><p>Lorem ipsum dolor sit amet, consectetur adipiscing elit, sed do eiusmod tempor incididunt ut labore et dolore magna aliqua.</p></div>
  </div>
  <div class="foot"></div><div class="foot-tag">Talvorix</div>
</section>

<section class="slide" style="left:18px;top:2348px">
  <div class="heading"><b>Lorem ipsum</b> dolor sit amet</div>
  <div style="position:absolute;left:30px;top:70px;width:200px;height:200px;background:linear-gradient(90deg,#cfd3cc,#6aa84f 25%,#1d3a19 45%,#c9a227 65%,#e0b830 85%,#cfd3cc)" role="img" aria-label="Four test tubes in a rack filled with green and yellow liquid"></div>
  <div style="position:absolute;left:290px;top:50px;width:2px;height:230px;background:#ccc"></div>
  <div style="position:absolute;left:284px;top:66px;display:flex;flex-direction:column;gap:38px">
    <span style="width:14px;height:14px;border-radius:50%;background:var(--green-mid)"></span>
    <span style="width:14px;height:14px;border-radius:50%;background:var(--green-dark)"></span>
    <span style="width:14px;height:14px;border-radius:50%;background:#a8881d"></span>
    <span style="width:14px;height:14px;border-radius:50%;background:var(--gold)"></span>
  </div>
  <div style="position:absolute;left:316px;top:62px;width:230px;display:flex;flex-direction:column;gap:22px">
    <p>Lorem ipsum dolor sit amet, consectetur adipiscing elit, sed do eiusmod tempor incididunt ut labore et dolore magna aliqua.</p>
    <p>Lorem ipsum dolor sit amet, consectetur adipiscing elit, sed do eiusmod tempor incididunt ut labore et dolore magna aliqua.</p>
    <p>Lorem ipsum dolor sit amet, consectetur adipiscing elit, sed do eiusmod tempor incididunt ut labore et dolore magna aliqua.</p>
    <p>Lorem ipsum dolor sit amet, consectetur adipiscing elit, sed do eiusmod tempor incididunt ut labore et dolore magna aliqua.</p>
  </div>
  <div class="foot"></div><div class="foot-tag">Talvorix</div>
</section>

<section class="slide" style="left:614px;top:2348px">
  <div class="heading"><b>Lorem ipsum</b> dolor sit amet</div>
  <svg style="position:absolute;left:30px;top:60px" width="140" height="180" viewBox="0 0 140 180">
    <g font-family="Open Sans, Arial, sans-serif" font-size="9" font-weight="700" fill="#333" text-anchor="middle">
      <text x="16" y="10">50%</text><text x="66" y="10">35%</text><text x="116" y="10">100%</text>
    </g>
    <rect x="4" y="16" width="24" height="160" fill="#e0e0e0"/><rect x="4" y="96" width="24" height="80" fill="#6aa84f"/>
    <rect x="54" y="16" width="24" height="160" fill="#e0e0e0"/><rect x="54" y="120" width="24" height="56" fill="#6aa84f"/>
    <rect x="104" y="16" width="24" height="160" fill="#6aa84f"/>
    <g stroke="#fff" stroke-width="2">
      <path d="M4 26h24M4 36h24M4 46h24M4 56h24M4 66h24M4 76h24M4 86h24M4 106h24M4 116h24M4 126h24M4 136h24M4 146h24M4 156h24M4 166h24"/>
      <path d="M54 26h24M54 36h24M54 46h24M54 56h24M54 66h24M54 76h24M54 86h24M54 96h24M54 106h24M54 130h24M54 140h24M54 150h24M54 160h24M54 170h24"/>
      <path d="M104 26h24M104 36h24M104 46h24M104 56h24M104 66h24M104 76h24M104 86h24M104 96h24M104 106h24M104 116h24M104 126h24M104 136h24M104 146h24M104 156h24M104 166h24"/>
    </g>
  </svg>
  <div style="position:absolute;left:26px;top:248px;width:160px;display:grid;grid-template-columns:repeat(3,1fr);gap:6px;text-align:center"><p>Lorem ipsum dolor sit amet</p><p>Lorem ipsum dolor sit amet</p><p>Lorem ipsum dolor sit amet</p></div>
  <svg style="position:absolute;left:230px;top:120px" width="320" height="110" viewBox="0 0 320 110">
    <path d="M0 110V55l30-15 30 20 35-30 40 25 30-20 40 15 35-35 40 25 40-15v90z" fill="#a9cf8f"/>
    <path d="M0 110V75l40-10 35 15 40-20 40 15 40-10 40 15 45-20 40 10v40z" fill="#4f8f35"/>
    <path d="M0 110V92l50-8 40 10 50-12 50 12 50-8 80 6v18z" fill="#1d3a19"/>
  </svg>
  <p style="position:absolute;left:270px;top:240px;width:250px;text-align:center">Lorem ipsum dolor sit amet, consectetur adipiscing elit, sed do eiusmod tempor incididunt ut labore et dolore magna aliqua.</p>
  <div class="foot"></div><div class="foot-tag">Talvorix</div>
</section>

<section class="slide" style="left:18px;top:2677px">
  <div class="heading"><b>Lorem ipsum</b> dolor sit amet</div>
  <div class="col" style="left:16px;top:40px;width:280px"><p>Lorem ipsum dolor sit amet, consectetur adipiscing elit, sed do eiusmod tempor incididunt ut labore et dolore magna aliqua. Ut enim ad minim veniam, quis nostrud exercitation ullamco laboris nisi ut aliquip ex ea commodo consequat.</p></div>
  <div class="panel-dark" style="left:16px;top:110px;width:264px;height:70px;padding:14px 16px"><p style="color:#dbe8d3">Lorem ipsum dolor sit amet, consectetur adipiscing elit, sed do eiusmod tempor incididunt ut labore et dolore magna aliqua. Ut enim ad minim veniam, quis nostrud exercitation ullamco laboris nisi ut aliquip ex ea.</p></div>
  <div class="col" style="left:16px;top:200px;width:280px"><p>Lorem ipsum dolor sit amet, consectetur adipiscing elit, sed do eiusmod tempor incididunt ut labore et dolore magna aliqua. Ut enim ad minim veniam, quis nostrud exercitation ullamco laboris nisi ut aliquip ex ea commodo consequat.</p></div>
  <div class="photo" style="left:320px;top:0;width:248px;height:160px" role="img" aria-label="Business meeting over documents and laptop"></div>
  <div class="panel-dark" style="left:310px;top:150px;width:258px;height:160px;padding:26px 40px;text-align:center">
    <div style="font-family:Montserrat,Arial,sans-serif;font-size:28px;font-weight:800;color:#fff;line-height:.8">&ldquo;</div>
    <div style="color:#fff;font-size:7.5px;line-height:1.5;margin-top:6px">Lorem ipsum dolor sit amet, consectetur adipiscing elit, sed do eiusmod tempor incididunt ut labore et dolore magna aliqua.</div>
  </div>
  <div class="foot"></div><div class="foot-tag">Talvorix</div>
</section>

<section class="slide" style="left:614px;top:2677px">
  <div class="heading" style="font-size:10px"><b>Management Team</b></div>
  <div class="tile-art" style="left:310px;top:0;width:258px;height:150px;clip-path:polygon(15% 0,100% 0,100% 100%,40% 60%)" role="img" aria-label="Decorative grey and green tile mosaic"></div>
  <div style="position:absolute;left:24px;right:24px;top:90px;display:grid;grid-template-columns:repeat(3,1fr);gap:24px;text-align:center">
    <div><div class="member-photo" role="img" aria-label="Portrait of the executive vice president"></div><div class="member-name">Daniel Reyes</div><div class="member-role">Executive Vice President</div><p style="margin-top:3px">Daniel has held several senior executive roles in pharmacy benefit management over many years in Brookfield, NJ.</p></div>
    <div><div class="member-photo" role="img" aria-label="Portrait of the president"></div><div class="member-name">Owen Whitfield</div><div class="member-role">President</div><p style="margin-top:3px">Owen has over 25 years of experience in the healthcare industry and has held numerous positions in the field.</p></div>
    <div><div class="member-photo" role="img" aria-label="Portrait of the senior vice president"></div><div class="member-name">Colin Barrett</div><div class="member-role">Senior Vice President</div><p style="margin-top:3px">Colin has over 15 years of experience in client services and clinical pharmacy solutions and analytics.</p></div>
  </div>
  <div class="foot"></div><div class="foot-tag">Talvorix</div>
</section>

<section class="slide" style="left:289px;top:3018px;width:620px;height:378px">
  <div style="position:absolute;left:0;right:0;top:0;height:6px;background:var(--green)"></div>
  <div class="brand" style="position:absolute;left:0;right:0;top:40px;justify-content:center;font-size:42px"><i style="width:24px;height:24px"></i>Talvorix</div>
  <div style="position:absolute;left:0;right:0;top:98px;text-align:center;font-size:6.5px;color:#555">prescription benefit management</div>
  <div style="position:absolute;left:0;right:0;top:108px;text-align:center;font-family:Montserrat,Arial,sans-serif;font-weight:800;font-size:30px;color:var(--green)">THANK YOU!</div>
  <div style="position:absolute;left:0;right:0;top:172px;bottom:0;background:var(--green-pale)"></div>
  <div style="position:absolute;left:20px;right:20px;top:190px;bottom:40px;background:#eef5e8;display:grid;grid-template-columns:repeat(4,1fr);text-align:center;padding-top:28px;font-size:9px;color:#222">
    <div><svg width="30" height="30" viewBox="0 0 24 24"><path d="M6 2l4 4-2 3c1 2 3 4 5 5l3-2 4 4-3 4C9 20 4 15 2 5z" fill="#333"/></svg><div style="margin-top:14px">555-010-4477</div></div>
    <div><svg width="32" height="30" viewBox="0 0 26 20"><rect x="1" y="1" width="24" height="18" fill="none" stroke="#333" stroke-width="1.5"/><path d="M1 1l12 10L25 1" fill="none" stroke="#333" stroke-width="1.5"/></svg><div style="margin-top:14px">info@talvorixrx.com</div></div>
    <div><svg width="24" height="30" viewBox="0 0 16 22"><path d="M8 1a7 7 0 00-7 7c0 5 7 13 7 13s7-8 7-13a7 7 0 00-7-7z" fill="none" stroke="#333" stroke-width="1.5"/><circle cx="8" cy="8" r="2.5" fill="#333"/></svg><div style="margin-top:8px;line-height:1.35">Talvorix, Inc.<br>PO Box 118<br>Fairview, NY 10000<br>555-010-4477</div></div>
    <div><svg width="30" height="30" viewBox="0 0 24 24"><circle cx="12" cy="12" r="10" fill="none" stroke="#333" stroke-width="1.5"/><path d="M2 12h20M12 2c-4 5-4 15 0 20M12 2c4 5 4 15 0 20" fill="none" stroke="#333" stroke-width="1.5"/></svg><div style="margin-top:14px">http://www.talvorixrx.com</div></div>
  </div>
  <div style="position:absolute;left:0;right:0;bottom:0;height:12px;background:var(--green)"></div>
  <div class="foot-tag" style="bottom:5px">Talvorix</div>
</section>

</body>
</html>
```